The Web Promotion Playbook for Yard & Patio Construction Crews

We need a book cover design that is for a book targeting landscape and outdoor living contractors that helps them grow their business using online marketing.

We run a business focused on this industry so you can see what we do: https://yardcrewgrowthworks.com/

The title is: The Web Promotion Playbook for Yard & Patio Construction Crews

The author is: Trent Varnholm
Some drafts have been done however they're still looking basic and somewhat amateur, we're looking for something that will stand out.

Target Market(s)

Landscape, Hardscape and Outdoor Living Contractors and Business Owners

Industry/Entity Type

Online Marketing

Font styles to use
Serif
Sans Serif

Requirements
Must have
• The part of the title that should stand out the most is the text "Web Promotion Playbook".
Should not have
• The color red

```html
<!DOCTYPE html>
<html lang="en">
<head>
<meta charset="utf-8">
<title>The Web Promotion Playbook for Yard &amp; Patio Construction Crews — Trent Varnholm</title>
<link rel="stylesheet" href="https://fonts.googleapis.com/css2?family=Oswald:wght@700&family=Montserrat:wght@700;800;900&display=swap">
<style>
  :root {
    --page-bg: #e9e9e9;
    --cover-bg: #ffffff;
    --ink: #111111;
    --green-deep: #2a8a12;
    --green-lime: #97b70a;
    --pill-green: #1a8a3c;
    --pill-text: #ffff00;
    --band-green: rgba(22, 112, 30, 0.88);
    --author-first: #ffee00;
    --author-last: #ffffff;
  }
  html, body {
    margin: 0;
    width: 1200px;
    height: 1200px;
    overflow: hidden;
    background: var(--page-bg);
  }
  .cover {
    position: absolute;
    left: 210px;
    top: 15px;
    width: 780px;
    height: 1170px;
    background: var(--cover-bg);
    overflow: hidden;
  }
  .cover-scene {
    position: absolute;
    left: 0;
    top: 600px;
    width: 780px;
    height: 570px;
    background:
      linear-gradient(to bottom, rgba(255,255,255,1) 0%, rgba(255,255,255,0.55) 12%, rgba(255,255,255,0) 28%),
      radial-gradient(ellipse at 72% 55%, #5d8a7a 0%, #3f6a5a 22%, rgba(63,106,90,0) 40%),
      linear-gradient(100deg, #6cc21e 0%, #4fa41a 35%, #88c83a 55%, #3d7d2a 100%);
  }
  .cover-title {
    position: absolute;
    left: 0;
    top: 0;
    width: 780px;
    height: 680px;
  }
  .title-small { font-family: "Montserrat", sans-serif; font-weight: 900; fill: var(--ink); }
  .title-rule { stroke: var(--ink); stroke-width: 2.5; }
  .title-key { font-family: "Oswald", sans-serif; font-weight: 700; fill: var(--green-deep); }
  .title-audience { font-family: "Oswald", sans-serif; font-weight: 700; fill: var(--green-lime); }
  .title-pill { fill: var(--pill-green); }
  .title-pill-text { font-family: "Oswald", sans-serif; font-weight: 700; fill: var(--pill-text); }
  .author-band {
    position: absolute;
    left: 0;
    top: 1096px;
    width: 780px;
    height: 74px;
    background: var(--band-green);
    display: flex;
    align-items: center;
    justify-content: center;
    font-family: "Montserrat", sans-serif;
    font-weight: 700;
    font-size: 36px;
    letter-spacing: 0.32em;
  }
  .author-first { color: var(--author-first); margin-right: 0.5em; }
  .author-last { color: var(--author-last); }
</style>
</head>
<body>
  <div class="cover">
    <div class="cover-scene" role="img" aria-label="Landscaped park with a winding stone path, trimmed shrubs, lawns, trees and a reflecting pond"></div>

    <svg class="cover-title" viewBox="0 0 780 680" xmlns="http://www.w3.org/2000/svg">
      <line class="title-rule" x1="34" y1="55" x2="326" y2="55"/>
      <text class="title-small" x="392" y="70" font-size="40" text-anchor="middle">THE</text>
      <line class="title-rule" x1="456" y1="55" x2="752" y2="55"/>

      <text class="title-key" x="51" y="162" font-size="112" textLength="679" lengthAdjust="spacingAndGlyphs">WEB PROMOTION</text>
      <text class="title-key" x="51" y="292" font-size="156" textLength="679" lengthAdjust="spacingAndGlyphs">PLAYBOOK</text>

      <line class="title-rule" x1="34" y1="321" x2="326" y2="321"/>
      <text class="title-small" x="392" y="337" font-size="38" text-anchor="middle">FOR</text>
      <line class="title-rule" x1="456" y1="321" x2="752" y2="321"/>

      <text class="title-audience" x="112" y="446" font-size="134" textLength="556" lengthAdjust="spacingAndGlyphs">YARD &amp; PATIO</text>
      <text class="title-audience" x="51" y="559" font-size="134" textLength="679" lengthAdjust="spacingAndGlyphs">CONSTRUCTION</text>

      <rect class="title-pill" x="173" y="574" width="433" height="87" rx="18"/>
      <text class="title-pill-text" x="389.5" y="646" font-size="82" text-anchor="middle">CREWS</text>
    </svg>

    <div class="author-band">
      <span class="author-first">TRENT</span><span class="author-last">VARNHOLM</span>
    </div>
  </div>
</body>
</html>
```